Save our Business Card - We need your help

We need a fresh look on our business cards. We like it as it is, but it's not quite getting the 'wow' effect that we desire.
We're a tech startup building a cloud based solution for retailers consisting of Point of Sale, Inventory management and CRM.
The design should communicate a sense of a company that cares about the little things, design and relationships.
You can have a look at our website www.tillnest.com to get a feel for what we're like. Please feel free to message us for any further clarification
Target Market(s)
Our Customers are retail busines owners, cafe owners, other startups etc.
Industry/Entity Type
Building
Colors
Designer to choose colors to be used in the design.
Look and feel
Each slider illustrates characteristics of the customer's brand and the style your logo design should communicate.

```html
<!DOCTYPE html>
<html lang="en">
<head>
<meta charset="utf-8">
<title>TillNest Business Card</title>
<link href="https://fonts.googleapis.com/css2?family=Arimo:wght@400;700&display=swap" rel="stylesheet">
<style>
  :root{
    --bg:#e9e6e2;
    --card-white:#ffffff;
    --card-black:#050505;
    --orange:#f7941d;
    --ink:#1a1a1a;
    --muted:#444444;
  }
  *{margin:0;padding:0;box-sizing:border-box}
  html,body{width:1200px;height:848px;overflow:hidden}
  body{background:var(--bg);font-family:"Arimo",Arial,sans-serif;position:relative}
  .card{position:absolute;top:272px;width:530px;height:303px;box-shadow:0 6px 18px rgba(0,0,0,.18)}
  .card-front{left:46px;background:var(--card-white);overflow:hidden}
  .card-back{left:624px;background:var(--card-black);display:flex;align-items:center;justify-content:center;gap:20px}

  .side-band{position:absolute;left:10px;top:0;width:44px;height:100%;background:var(--card-black)}

  .brand{position:absolute;left:78px;top:36px;display:flex;align-items:center;gap:14px}
  .brand-mark{width:54px;height:54px;background:var(--orange)}
  .brand-name{font-weight:700;font-size:40px;color:var(--orange);letter-spacing:.5px}

  .holder{position:absolute;right:34px;top:58px;text-align:right}
  .holder-name{font-size:19px;color:var(--ink);letter-spacing:.3px;padding:0 2px 5px 10px;border-bottom:2px solid var(--orange)}
  .holder-role{font-size:11px;color:var(--ink);margin-top:5px}

  .contacts{position:absolute;left:80px;bottom:26px;list-style:none}
  .contacts li{display:flex;align-items:flex-start;gap:12px;font-size:14px;color:var(--ink);line-height:18px;margin-top:6px}
  .contacts svg{width:16px;height:16px;flex:none;margin-top:1px}

  .card-back .brand-mark{width:110px;height:110px}
  .card-back .brand-name{font-size:66px}
</style>
</head>
<body>
  <section class="card card-front" aria-label="Business card front">
    <div class="side-band"></div>
    <div class="brand">
      <div class="brand-mark"></div>
      <span class="brand-name">TillNest</span>
    </div>
    <div class="holder">
      <div class="holder-name">JANE ROWE</div>
      <div class="holder-role">Manager</div>
    </div>
    <ul class="contacts">
      <li>
        <svg viewBox="0 0 16 16" aria-hidden="true"><path fill="#f7941d" d="M2 6c0-2 2-3 6-3s6 1 6 3v1h-3V5.5H5V7H2zM4 8h8l1 5H3z"/><circle cx="8" cy="10.5" r="1.5" fill="#fff"/></svg>
        <span>+(603) 4180 2267</span>
      </li>
      <li>
        <svg viewBox="0 0 16 16" aria-hidden="true"><rect x="1" y="3" width="14" height="10" fill="#f7941d"/><path d="M1 3l7 6 7-6" fill="none" stroke="#fff" stroke-width="1.2"/></svg>
        <span>Email hello@tillnest.com</span>
      </li>
      <li>
        <svg viewBox="0 0 16 16" aria-hidden="true"><g fill="none" stroke="#f7941d" stroke-width="1.3"><circle cx="8" cy="8" r="6.5"/><ellipse cx="8" cy="8" rx="3" ry="6.5"/><path d="M1.5 8h13M2.5 4.8h11M2.5 11.2h11"/></g></svg>
        <span>www.tillnest.com</span>
      </li>
      <li>
        <svg viewBox="0 0 16 16" aria-hidden="true"><path fill="#f7941d" d="M8 1a5 5 0 0 1 5 5c0 4-5 9-5 9S3 10 3 6a5 5 0 0 1 5-5z"/><circle cx="8" cy="6" r="1.8" fill="#fff"/></svg>
        <span>Unit B-2-14, Block A8 Harbourline Avenue Jalan Kenari 5<br>47100 Puchong, Selangor, Malaysia</span>
      </li>
    </ul>
  </section>

  <section class="card card-back" aria-label="Business card back">
    <div class="brand-mark"></div>
    <span class="brand-name">TillNest</span>
  </section>
</body>
</html>
```